QuorintaFields background design

The task is to create a modern looking and very attractive background for the quorintaFields laboratory results reports + cover-page for the reports that matches the same design.

The background should be beautiful but also minimalistic enough not to interfere with the content inside the reports. If the background behind the content is too intensive then it is difficult to read the content. Our LOGO is blue and we have used blue-ish colors so far so perhaps one should try to keep blue at least as one of the colors. We have preferred to keep the design abstract/minimalistic rather than using photos.

Please look at the attached files, especially the file "Report with the current background" where you will see how the content is layed inside the reports. You will also see the current background that we would like to change. Then there is a file that contains the report pages without background that you could use to present the background.

```html
<!DOCTYPE html>
<html lang="en">
<head>
<meta charset="utf-8">
<title>QuorintaFields – Laboratory Test Results</title>
<link href="https://fonts.googleapis.com/css2?family=Open+Sans:wght@300;400;600;700&display=swap" rel="stylesheet">
<style>
  :root{
    --blue-deep:#0b6cc4;
    --blue-mid:#1a8ad6;
    --blue-light:#33b8f2;
    --blue-pale:#bfe3f7;
    --grey-arc:#d2d4d6;
    --ink:#3a3a3a;
    --ink-soft:#4a4a4a;
    --label:#555;
    --pin:#9a9a9a;
    --red:#e8302a;
    --orange:#f39a1e;
    --yellow:#f5cf16;
    --green:#3aac4a;
  }
  *{box-sizing:border-box;margin:0;padding:0}
  html,body{width:848px;height:1200px;overflow:hidden;background:#fff}
  body{font-family:"Open Sans",Arial,sans-serif;color:var(--ink)}
  .page{position:relative;width:848px;height:1200px;overflow:hidden;background:#fff}
  .backdrop{position:absolute;inset:0;width:848px;height:1200px}
  .brand{position:absolute;left:606px;top:74px;width:164px;height:164px;border-radius:50%;
    display:flex;align-items:center;justify-content:center}
  .brand-name{font-size:17px;font-weight:600;color:var(--blue-mid);letter-spacing:-.2px}
  .page-title{position:absolute;left:60px;top:192px;font-weight:300;font-size:26px;letter-spacing:.3px;color:#333}
  .result{position:absolute;width:343px}
  .result-head{display:flex;justify-content:space-between;align-items:baseline;height:20px}
  .result-name{font-size:15px;font-weight:600;color:#333}
  .result-value{font-size:12px;font-weight:600;color:#333}
  .result-value sup{font-size:8px}
  .scale{position:relative;margin:24px 5px 0 5px;height:5px}
  .scale-bar{display:flex;gap:2px;height:5px}
  .scale-bar span{flex:1;border-radius:3px}
  .pin{position:absolute;bottom:7px;width:13px;height:19px;transform:translateX(-50%)}
  .scale-labels{position:relative;height:18px;margin-top:10px;font-size:12px;color:var(--label)}
  .scale-labels span{position:absolute;top:0}
  .scale-labels .lo{left:3px}
  .scale-labels .mid{left:50%;transform:translateX(-50%)}
  .scale-labels .hi{right:2px}
  .result-text{margin-top:11px;font-size:12.4px;line-height:18.7px;color:var(--ink-soft);text-align:justify}
  .seg-low{background:linear-gradient(90deg,var(--red),var(--orange) 45%,var(--yellow))}
  .seg-ok{background:var(--green)}
  .seg-high{background:linear-gradient(90deg,var(--yellow),var(--orange) 55%,var(--red))}
  .seg-green-yellow{background:linear-gradient(90deg,var(--green) 60%,var(--yellow))}
  .seg-yellow-red{background:linear-gradient(90deg,var(--yellow),var(--orange) 45%,var(--red))}
  .seg-red-yellow{background:linear-gradient(90deg,var(--red),var(--orange) 45%,var(--yellow))}
  .seg-yellow-green{background:linear-gradient(90deg,var(--yellow),var(--green) 40%)}
  .footer{position:absolute;right:62px;top:1163px;font-size:12px;color:#333}
</style>
</head>
<body>
<div class="page">
  <svg class="backdrop" viewBox="0 0 848 1200" aria-hidden="true">
    <defs>
      <linearGradient id="topSweep" x1="0" y1="0" x2="1" y2="0">
        <stop offset="0" stop-color="#4fb4e8"/>
        <stop offset="0.5" stop-color="#1e8fdb"/>
        <stop offset="1" stop-color="#0b6cc4"/>
      </linearGradient>
      <linearGradient id="bottomSweep" x1="0" y1="0" x2="1" y2="0">
        <stop offset="0" stop-color="#0f74cc"/>
        <stop offset="1" stop-color="#2ea3e6"/>
      </linearGradient>
    </defs>
    <!-- top sweep -->
    <path d="M0 0 H848 V310 C790 190 640 90 380 58 C240 42 110 52 0 70 Z" fill="url(#topSweep)"/>
    <path d="M0 40 C160 28 330 36 470 62 C350 52 180 52 0 76 Z" fill="#9fd4f2" opacity=".8"/>
    <path d="M0 58 C150 46 300 50 420 64 C300 60 150 64 0 82 Z" fill="#d9eef9"/>
    <path d="M0 70 C110 52 240 42 380 58 C640 90 790 190 848 310 V318 C780 200 620 104 380 72 C240 56 110 66 0 86 Z" fill="#ffffff"/>
    <path d="M520 70 C680 110 790 190 848 290 V300 C790 200 690 130 520 78 Z" fill="#d7ecf8"/>
    <!-- emblem rings -->
    <circle cx="688" cy="156" r="105" fill="none" stroke="var(--grey-arc)" stroke-width="12" stroke-dasharray="330 400" transform="rotate(70 688 156)"/>
    <circle cx="688" cy="156" r="92" fill="var(--blue-light)"/>
    <circle cx="688" cy="156" r="82" fill="#ffffff"/>
    <!-- bottom sweep -->
    <path d="M0 1068 C140 1100 320 1150 470 1200 H0 Z" fill="#cfe8f7"/>
    <path d="M0 1090 C140 1118 300 1160 420 1200 H0 Z" fill="url(#bottomSweep)"/>
    <path d="M0 1132 C110 1150 220 1176 290 1200 H0 Z" fill="#0a63b8" opacity=".6"/>
  </svg>

  <div class="brand"><span class="brand-name">QuorintaFields</span></div>

  <h1 class="page-title">LABORATORY TEST RESULTS</h1>

  <section class="result" style="left:60px;top:270px">
    <div class="result-head"><span class="result-name">Glucose</span><span class="result-value">78 mg/dl</span></div>
    <div class="scale">
      <svg class="pin" style="left:50%" viewBox="0 0 13 19"><path d="M6.5 1.2a5.3 5.3 0 0 1 5.3 5.3c0 3.6-5.3 11-5.3 11S1.2 10.1 1.2 6.5a5.3 5.3 0 0 1 5.3-5.3z" fill="#fff" stroke="var(--pin)" stroke-width="1.6"/><circle cx="6.5" cy="6.5" r="2" fill="none" stroke="var(--pin)" stroke-width="1.3"/></svg>
      <div class="scale-bar"><span class="seg-low"></span><span class="seg-ok"></span><span class="seg-high"></span></div>
    </div>
    <div class="scale-labels"><span class="lo">low</span><span class="mid">normal 60-99</span><span class="hi">high</span></div>
    <p class="result-text">Glucose is the main source of energy for the body. The danger of continuously high blood glucose is that sugar coats the red blood cells, causing them to become stiff and "sticky". These cells interfere with proper blood circulation and cause build-up on blood vessels. High blood sugar can lead to cardiovascular and kidney disease, blindness, or ulcers.</p>
  </section>

  <section class="result" style="left:444px;top:270px">
    <div class="result-head"><span class="result-name">C-reactive protein</span><span class="result-value">1.2 mg/l</span></div>
    <div class="scale">
      <svg class="pin" style="left:7.5%" viewBox="0 0 13 19"><path d="M6.5 1.2a5.3 5.3 0 0 1 5.3 5.3c0 3.6-5.3 11-5.3 11S1.2 10.1 1.2 6.5a5.3 5.3 0 0 1 5.3-5.3z" fill="#fff" stroke="var(--pin)" stroke-width="1.6"/><circle cx="6.5" cy="6.5" r="2" fill="none" stroke="var(--pin)" stroke-width="1.3"/></svg>
      <div class="scale-bar"><span class="seg-green-yellow"></span><span class="seg-yellow-red"></span></div>
    </div>
    <div class="scale-labels"><span class="lo">normal ≤5</span><span class="hi">high</span></div>
    <p class="result-text">C-reactive protein (CRP) is a general inflammation marker. Any tissue injury or infection will raise the amount of CRP in the blood within a few hours. After the inflammation is gone, CRP goes down fast. Increased CRP levels not related to acute illness or infection have been linked to higher risk of heart disease.</p>
  </section>

  <section class="result" style="left:60px;top:526px">
    <div class="result-head"><span class="result-name">Sodium</span><span class="result-value">142 mmol/l</span></div>
    <div class="scale">
      <svg class="pin" style="left:55%" viewBox="0 0 13 19"><path d="M6.5 1.2a5.3 5.3 0 0 1 5.3 5.3c0 3.6-5.3 11-5.3 11S1.2 10.1 1.2 6.5a5.3 5.3 0 0 1 5.3-5.3z" fill="#fff" stroke="var(--pin)" stroke-width="1.6"/><circle cx="6.5" cy="6.5" r="2" fill="none" stroke="var(--pin)" stroke-width="1.3"/></svg>
      <div class="scale-bar"><span class="seg-low"></span><span class="seg-ok"></span><span class="seg-high"></span></div>
    </div>
    <div class="scale-labels"><span class="lo">low</span><span class="mid">normal 136-146</span><span class="hi">high</span></div>
    <p class="result-text">The amount of sodium is closely related to the amount of water in the body. Excess levels may occur in dehydration, excess sodium in your diet or several diseases. Low levels may occur in cases of heart failure, severe sweating, diarrhea or vomiting, poor nutrition or drinking too much water.</p>
  </section>

  <section class="result" style="left:444px;top:526px">
    <div class="result-head"><span class="result-name">Potassium</span><span class="result-value">4.2 mmol/l</span></div>
    <div class="scale">
      <svg class="pin" style="left:49.5%" viewBox="0 0 13 19"><path d="M6.5 1.2a5.3 5.3 0 0 1 5.3 5.3c0 3.6-5.3 11-5.3 11S1.2 10.1 1.2 6.5a5.3 5.3 0 0 1 5.3-5.3z" fill="#fff" stroke="var(--pin)" stroke-width="1.6"/><circle cx="6.5" cy="6.5" r="2" fill="none" stroke="var(--pin)" stroke-width="1.3"/></svg>
      <div class="scale-bar"><span class="seg-low"></span><span class="seg-ok"></span><span class="seg-high"></span></div>
    </div>
    <div class="scale-labels"><span class="lo">low</span><span class="mid">normal 3.5-5.1</span><span class="hi">high</span></div>
    <p class="result-text">Potassium helps nerves and muscles communicate. Dehydration, diarrhea, and excessive sweating are common causes of low potassium levels. Changes in potassium level alter the activity of nerves and muscles, especially the heart: low levels can lead to an irregular heartbeat and high levels cause decreased heart muscle activity.</p>
  </section>

  <section class="result" style="left:60px;top:780px">
    <div class="result-head"><span class="result-name">Creatinine</span><span class="result-value">1.1 mg/dl</span></div>
    <div class="scale">
      <svg class="pin" style="left:62.5%" viewBox="0 0 13 19"><path d="M6.5 1.2a5.3 5.3 0 0 1 5.3 5.3c0 3.6-5.3 11-5.3 11S1.2 10.1 1.2 6.5a5.3 5.3 0 0 1 5.3-5.3z" fill="#fff" stroke="var(--pin)" stroke-width="1.6"/><circle cx="6.5" cy="6.5" r="2" fill="none" stroke="var(--pin)" stroke-width="1.3"/></svg>
      <div class="scale-bar"><span class="seg-low"></span><span class="seg-ok"></span><span class="seg-high"></span></div>
    </div>
    <div class="scale-labels"><span class="lo">low</span><span class="mid">normal 0.7-1.2</span><span class="hi">high</span></div>
    <p class="result-text">Creatinine is critical for evaluating renal function. Your serum creatinine is a waste product that is formed when muscle cells break down in your blood. It is produced by muscles as it depends on muscle mass and protein intake. High levels could indicate kidney dysfunction while decreased levels may reflect low muscle mass.</p>
  </section>

  <section class="result" style="left:444px;top:780px">
    <div class="result-head"><span class="result-name">EGFR</span><span class="result-value">98 ml/min/1.73 m<sup>2</sup></span></div>
    <div class="scale">
      <svg class="pin" style="left:83%" viewBox="0 0 13 19"><path d="M6.5 1.2a5.3 5.3 0 0 1 5.3 5.3c0 3.6-5.3 11-5.3 11S1.2 10.1 1.2 6.5a5.3 5.3 0 0 1 5.3-5.3z" fill="#fff" stroke="var(--pin)" stroke-width="1.6"/><circle cx="6.5" cy="6.5" r="2" fill="none" stroke="var(--pin)" stroke-width="1.3"/></svg>
      <div class="scale-bar"><span class="seg-red-yellow"></span><span class="seg-yellow-green"></span></div>
    </div>
    <div class="scale-labels"><span class="lo">low</span><span class="hi">normal &gt;60</span></div>
    <p class="result-text">An estimated glomerular filtration rate (eGFR) is calculated according to your creatinine level, age, sex and race. The eGFR is used to screen for and detect early kidney damage and to monitor kidney status. An eGFR below 60 mL/min suggests that some kidney damage has occurred.</p>
  </section>

  <div class="footer">Marcus Ellery / 11.09.2017 / Page 2</div>
</div>
</body>
</html>
```